Supplement Bottle Packaging and Design

We want to rebrand our current health supplements (see below). We do want it to be modern, vibrant and appealing supplement bottles. Very upscale and elegant as it targets primarily women.
NOTE: READ THE ATTACHED WORD DOCUMENT!
Bottle size: We are totally open to the bottle size and shape, as long it's a typical supplement bottle size to handle 90-120 capsules; what we mostly need is new bottle design/packaging. YOU DON’T HAVE TO USE THE CURRENT WHITE BOTTLE SHAPE, BUT ANYTHING MORE MODERN WOULD WORK!
Updates
We need more modern, clean sleek designs to choose from
Look and feel
Each slider illustrates characteristics of the customer's brand and the style your logo design should communicate.

```html
<!DOCTYPE html>
<html lang="en">
<head>
<meta charset="utf-8">
<title>Supplement Label Range</title>
<link href="https://fonts.googleapis.com/css2?family=Cormorant+Garamond:wght@400;500&family=Josefin+Sans:wght@700&display=swap" rel="stylesheet">
<style>
  :root {
    --ink-light: #fde9ee;
    --accent-gold: #eaa54a;
    --sugar-main: #37546b;
    --sugar-side: #4f7490;
    --hormone-main: #386f47;
    --hormone-side: #589b69;
    --tummy-main: #701828;
    --tummy-side: #ab5464;
    --liver-main: #935675;
    --liver-side: #ae6f92;
  }
  * { margin: 0; padding: 0; box-sizing: border-box; }
  html, body { width: 1200px; height: 1200px; overflow: hidden; background: #ffffff; }
  .label-range { width: 1200px; height: 1200px; display: flex; flex-direction: column; }
  .label { height: 300px; display: flex; color: var(--ink-light); font-family: "Cormorant Garamond", serif; }
  .label-front { position: relative; width: 745px; height: 100%; background: var(--main); }
  .label-side { flex: 1; position: relative; background: var(--side); }
  .nutrition-note { position: absolute; right: 0; top: 142px; font-size: 9px; white-space: nowrap; }
  .benefit-tag {
    position: absolute; left: 10px; top: 12px; padding-left: 9px;
    border-left: 2px solid var(--ink-light);
    font-size: 17px; line-height: 0.95; font-weight: 400;
  }
  .info-block { position: absolute; left: 320px; top: 12px; width: 250px; }
  .info-title { font-size: 13px; font-weight: 500; margin-bottom: 6px; }
  .info-copy { font-size: 10.5px; line-height: 1.4; }
  .capsule-count { display: flex; align-items: center; gap: 10px; margin-top: 8px; font-size: 11.5px; }
  .capsule-count::before { content: ""; width: 26px; height: 3px; background: var(--ink-light); }
  .product-name {
    position: absolute; left: 12px; bottom: 10px; display: flex; align-items: flex-end; gap: 8px;
  }
  .product-title {
    font-family: "Josefin Sans", sans-serif; font-weight: 700; line-height: 0.85;
    letter-spacing: -0.02em; text-transform: uppercase;
  }
  .brand-name { font-size: 10px; line-height: 1; padding-bottom: 4px; }
  .label--sugar { --main: var(--sugar-main); --side: var(--sugar-side); }
  .label--sugar .product-title { font-size: 52px; }
  .label--hormone { --main: var(--hormone-main); --side: var(--hormone-side); }
  .label--hormone .product-title { font-size: 56px; }
  .label--tummy { --main: var(--tummy-main); --side: var(--tummy-side); }
  .label--tummy .product-title { font-size: 74px; }
  .label--tummy .info-title, .label--tummy .capsule-count { color: var(--accent-gold); }
  .label--liver { --main: var(--liver-main); --side: var(--liver-side); }
  .label--liver .product-title { font-size: 82px; }
</style>
</head>
<body>
<main class="label-range">

  <section class="label label--sugar">
    <div class="label-front">
      <p class="benefit-tag">Support Healthy<br>Blood Glucose Levels*</p>
      <div class="info-block">
        <p class="info-title">Dietary Supplement</p>
        <p class="info-copy">Your hormone works hard every day—filtering toxins, supporting digestion, and keeping your body balanced. Give it the care it deserves with our Hormone Support Supplement</p>
        <p class="capsule-count">120 Vegetable Capsules</p>
      </div>
      <div class="product-name">
        <h2 class="product-title">Blood<br>Sugar</h2>
        <span class="brand-name">Clear<br>Blend</span>
      </div>
    </div>
    <div class="label-side"><span class="nutrition-note">Nutrition Information</span></div>
  </section>

  <section class="label label--hormone">
    <div class="label-front">
      <p class="benefit-tag">Support Healthy<br>Hormone Levels*</p>
      <div class="info-block">
        <p class="info-title">Dietary Supplement</p>
        <p class="info-copy">Your hormone works hard every day—filtering toxins, supporting digestion, and keeping your body balanced. Give it the care it deserves with our Hormone Support Supplement</p>
        <p class="capsule-count">120 Vegetable Capsules</p>
      </div>
      <div class="product-name">
        <h2 class="product-title">Hormone</h2>
        <span class="brand-name">Clear<br>Blend</span>
      </div>
    </div>
    <div class="label-side"><span class="nutrition-note">Nutrition Information</span></div>
  </section>

  <section class="label label--tummy">
    <div class="label-front">
      <p class="benefit-tag">Oxygenating Colon<br>Cleanse*</p>
      <div class="info-block">
        <p class="info-title">Dietary Supplement</p>
        <p class="info-copy">Your tummy works hard every day—filtering toxins, supporting digestion, and keeping your body balanced. Give it the care it deserves with our Tummy Support Supplement</p>
        <p class="capsule-count">120 Vegetable Capsules</p>
      </div>
      <div class="product-name">
        <h2 class="product-title">Tummy</h2>
        <span class="brand-name">Clear<br>Blend</span>
      </div>
    </div>
    <div class="label-side"><span class="nutrition-note">Nutrition Information</span></div>
  </section>

  <section class="label label--liver">
    <div class="label-front">
      <p class="benefit-tag">Rejuvenating Cleanse<br>&amp; Detox*</p>
      <div class="info-block">
        <p class="info-title">Dietary Supplement</p>
        <p class="info-copy">Your liver works hard every day—filtering toxins, supporting digestion, and keeping your body balanced. Give it the care it deserves with our Liver Support Supplement</p>
        <p class="capsule-count">120 Vegetable Capsules</p>
      </div>
      <div class="product-name">
        <h2 class="product-title">Liver</h2>
        <span class="brand-name">Clear<br>Blend</span>
      </div>
    </div>
    <div class="label-side"><span class="nutrition-note">Nutrition Information</span></div>
  </section>

</main>
</body>
</html>
```